2 Page Brochure - Commercial Roofing Company

We are looking for a double sided brochure, full color, for our commercial roofing company that tells customers a little bit about the company, what we do, and shows a few pictures.
The brochure would need to have our logo and color scheme that coordinates with that logo.
I have uploaded our logo, some ideas I had, and then the idea list also has our website on there if you'd like to take a look around there for some more ideas.
I have also uploaded some photos we'd like to use.
Page size should be 8.5" x 11".
Target Market(s)
Commercial Property Owners
Other font styles liked:
- Match logo font ideally so it's cohesive, but whatever looks best
Look and feel

```html
<!DOCTYPE html>
<html lang="en">
<head>
<meta charset="utf-8">
<title>Crestline Commercial – Brochure</title>
<link href="https://fonts.googleapis.com/css2?family=Poppins:wght@400;500;600;800&display=swap" rel="stylesheet">
<style>
  :root{
    --backdrop:#404040;
    --page:#262626;
    --page-shade:#2f2f2f;
    --orange:#ef5a28;
    --white:#ffffff;
    --text:#e8e8e8;
  }
  *{margin:0;padding:0;box-sizing:border-box}
  html,body{width:1200px;height:811px;overflow:hidden;background:var(--backdrop)}
  body{position:relative;font-family:'Poppins',sans-serif;color:var(--text)}
  .page{position:absolute;top:157px;width:385px;height:498px;background:var(--page);overflow:hidden}
  .page--front{left:189px}
  .page--back{left:622px}
  .page__art{position:absolute;inset:0;width:100%;height:100%}
  .brand{position:absolute;top:26px;right:26px;font-weight:600;font-size:13px;color:var(--white);letter-spacing:.2px;display:flex;align-items:center;gap:6px}
  .brand__mark{width:9px;height:9px;background:var(--orange)}
  .headline{position:absolute;left:160px;top:212px;font-weight:800;font-size:18.5px;line-height:22px;color:var(--white);
    -webkit-text-stroke:.6px #000;text-shadow:1px 1px 0 #000,-1px 1px 0 #000,1px -1px 0 #000,-1px -1px 0 #000}
  .section-title{font-weight:500;font-size:11.5px;color:var(--white);line-height:14px}
  .checklist{list-style:none;margin-top:9px}
  .checklist li{position:relative;padding-left:19px;font-size:7.4px;line-height:14.5px;color:var(--text)}
  .checklist li::before{content:"";position:absolute;left:2px;top:2.5px;width:4px;height:8px;border-right:2px solid var(--orange);border-bottom:2px solid var(--orange);transform:rotate(40deg)}
  .products{position:absolute;left:47px;top:303px}
  .services{position:absolute;left:209px;top:359px}
  .service-area{position:absolute;left:46px;top:40px;width:297px}
  .service-area__lead{font-weight:600;font-size:8.4px;color:var(--orange);margin-top:3px}
  .about{margin-top:12px;font-size:7.4px;line-height:10.7px;text-align:justify;color:var(--text)}
  .manufacturers{position:absolute;left:46px;top:243px}
  .contact{position:absolute;left:46px;top:413px;font-weight:600;font-size:7.2px;line-height:9.2px;color:var(--white)}
  .photo-ring{position:absolute;border-radius:50%;border:5px solid var(--orange);overflow:hidden}
  .photo-ring--roof{left:137px;top:206px;width:148px;height:148px;background:linear-gradient(160deg,#6b6d5a 0%,#e9eef2 35%,#f4f6f8 60%,#b89c76 100%)}
  .photo-ring--facade{left:149px;top:363px;width:110px;height:110px;background:linear-gradient(135deg,#8c7456 0%,#5d6066 45%,#7d6a55 100%)}
</style>
</head>
<body>

<section class="page page--front">
  <svg class="page__art" viewBox="0 0 612 792" preserveAspectRatio="none" aria-hidden="true">
    <defs>
      <linearGradient id="frontPhoto" x1="0" y1="0" x2="0" y2="1">
        <stop offset="0" stop-color="#b9c9d9"/>
        <stop offset=".35" stop-color="#d7dfe6"/>
        <stop offset=".55" stop-color="#5d4e47"/>
        <stop offset=".75" stop-color="#8a8480"/>
        <stop offset="1" stop-color="#6f6a66"/>
      </linearGradient>
    </defs>
    <polygon points="612,720 612,792 320,792" fill="#2e2e2e"/>
    <polygon points="0,5 612,215 612,565 0,355" fill="url(#frontPhoto)"/>
    <polygon points="15,0 612,150 612,215 0,5 0,0" fill="var(--orange)"/>
    <polygon points="0,355 612,562 612,572 0,420" fill="var(--orange)"/>
  </svg>
  <div role="img" aria-label="Photo of a company work truck parked beside a finished commercial building" style="position:absolute;left:0;top:20px;width:385px;height:300px"></div>
  <div class="brand"><span class="brand__mark"></span>Crestline Commercial</div>
  <h1 class="headline">Our specialty<br>is Commercial Roofs</h1>

  <div class="products">
    <h2 class="section-title">Our Products</h2>
    <ul class="checklist">
      <li>TPO</li><li>PVC</li><li>Modified Bitumen</li><li>Silicone Coatings</li><li>Acrylic Coatings</li>
      <li>Shingle</li><li>Metal</li><li>Tile</li><li>Spray Polyurethane Foam</li><li>And more</li>
    </ul>
  </div>

  <div class="services">
    <h2 class="section-title">Services We Offer</h2>
    <ul class="checklist">
      <li>New Roof Installation</li><li>Re-roofing</li><li>Roof Maintenance and Service</li>
      <li>Roof Inspections</li><li>Roof Coatings</li><li>And more</li>
    </ul>
  </div>
</section>

<section class="page page--back">
  <svg class="page__art" viewBox="0 0 385 498" aria-hidden="true">
    <polygon points="0,90 60,140 0,140" fill="var(--page-shade)"/>
    <polygon points="0,290 120,390 0,390" fill="var(--page-shade)"/>
    <polygon points="290,303 385,233 385,428 290,498" fill="var(--orange)"/>
  </svg>

  <div class="service-area">
    <h2 class="section-title">Service Area</h2>
    <p class="service-area__lead">We service the entire state of Arizona</p>
    <p class="about">Crestline Commercial opened the doors in 1984, and we’ve since installed, serviced, maintained, and coated thousands of commercial roofs around the state of Arizona, in the many climate regions of the state. Though we all live here for the constant sunshine, Arizona is one of the harshest environments in the US for roofs. Constant sun, heat, dryness, and then the torrential monsoon downpours all test the limits of your roof. We work with you to come up with a solution that works for your roof and will keep your business dry for years to come. Then, our team of project managers, superintendents, foremen, and field workers all come together to execute on that plan and install a quality roof. We are certified with many different manufacturers, so we’re able to offer custom solutions to solve your issues, that will also often come with reputable manufacturer warranties.</p>
  </div>

  <div class="manufacturers">
    <h2 class="section-title">Certified<br>Manufacturers</h2>
    <ul class="checklist">
      <li>Apex</li><li>Stratus</li><li>Nordline</li><li>Duraplane</li><li>Covex</li><li>Shieldtek</li><li>And more</li>
    </ul>
  </div>

  <div class="photo-ring photo-ring--roof" role="img" aria-label="Aerial photo of a white commercial flat roof"></div>
  <div class="photo-ring photo-ring--facade" role="img" aria-label="Photo of a roof edge and metal coping along a building"></div>

  <p class="contact">555-014-2290<br>www.crestline-az.com<br>AZ ROC 112233</p>
</section>

</body>
</html>
```